Happy Hour Invitation

Hello. The law firm I work for is throwing a happy hour for our providers. The information that should be on the invitation I will put below along with an example of how we want the invitations to look. The example invitation has gold line accents on the invitation. Instead of gold lines we would like blue lines. I will also add an attachment that shows the exact color blue in our logo. We understand that the invitation may not be exactly the same as the example, however, we want something similar. Very simple and very classy. If you could have 2 examples, one with a dark background and one with a light (off white) background. The color of the wording is a preference, but we would like to stick with the blue color if adding color. If you have any questions, please don't hesitate to ask.

Invitation information:
Brix9Legal
Happy Hour
The Quarry
18 Larkmoor Lane Suite 340
Frisco, TX 75219
January 9, 2025
6-9 pm
To RSVP send email to:
@marisol@brix9legal.example
Note: The Quarry had a clear bag policy

If possible, please shrink "the quarry bag policy" attachment and put that on the back of the invitation just the way it is.

```html
<!DOCTYPE html>
<html lang="en">
<head>
<meta charset="utf-8">
<title>Happy Hour Invitation — Front and Back</title>
<link rel="stylesheet" href="https://fonts.googleapis.com/css2?family=Marcellus&family=Barlow:wght@400;600;700&display=swap">
<style>
  :root {
    --stage-navy: #23305e;
    --card-light: #d8d5da;
    --card-dark: #000000;
    --accent-blue: #35c3ee;
    --poster-navy: #23305e;
    --poster-blue: #2fb4e6;
    --poster-white: #ffffff;
    --approve-green: #3bb54a;
    --prohibit-red: #e0252f;
    --ink-dark: #1f1f24;
  }
  html, body {
    margin: 0;
    padding: 0;
    width: 1200px;
    height: 1200px;
    overflow: hidden;
    background: var(--stage-navy);
  }
  .stage {
    position: relative;
    width: 1200px;
    height: 1200px;
  }
  .card {
    position: absolute;
    top: 273px;
    width: 509px;
    height: 654px;
    display: block;
  }
  .card--front { left: 65px; }
  .card--back { left: 624px; }
  .frame-line {
    fill: none;
    stroke: var(--accent-blue);
    stroke-width: 1.6;
  }
  .invite-text {
    font-family: "Marcellus", serif;
    fill: var(--accent-blue);
    text-anchor: middle;
  }
  .poster-text {
    font-family: "Barlow", sans-serif;
  }
  .poster-heading { font-weight: 700; fill: var(--poster-navy); }
  .poster-body { fill: var(--ink-dark); }
  .poster-light { fill: var(--poster-white); }
  .center { text-anchor: middle; }
</style>
</head>
<body>
<main class="stage">

  <!-- Front: invitation -->
  <svg class="card card--front" viewBox="0 0 820 1054" preserveAspectRatio="none" aria-label="Happy hour invitation, front">
    <rect width="820" height="1054" fill="var(--card-light)"/>
    <g class="frame-lines">
      <polyline class="frame-line" points="0,30 144,187"/>
      <polyline class="frame-line" points="553,0 553,140"/>
      <polyline class="frame-line" points="144,187 192,141 629,141 682,196 818,56"/>
      <polyline class="frame-line" points="144,187 144,693 194,750 0,953"/>
      <polyline class="frame-line" points="682,196 682,691 621,750 818,965"/>
      <polyline class="frame-line" points="682,691 769,785"/>
      <polyline class="frame-line" points="0,785 820,785"/>
      <polyline class="frame-line" points="221,785 404,985 404,1054"/>
      <polyline class="frame-line" points="553,843 553,1054"/>
    </g>

    <text class="invite-text firm-name" x="415" y="195" font-size="34">Brix9Legal</text>

    <g class="divider">
      <line class="frame-line" x1="254" y1="228" x2="398" y2="228"/>
      <circle class="frame-line" cx="415" cy="228" r="6"/>
      <line class="frame-line" x1="432" y1="228" x2="576" y2="228"/>
    </g>

    <text class="invite-text event-title" x="415" y="315" font-size="72">Happy Hour</text>

    <text class="invite-text venue" x="415" y="383" font-size="29">The Quarry</text>
    <text class="invite-text venue" x="415" y="423" font-size="29">18 Larkmoor Lane Suite 340</text>
    <text class="invite-text venue" x="415" y="462" font-size="29">Frisco, TX 75219</text>
    <text class="invite-text event-date" x="415" y="518" font-size="29">January 9, 2025</text>
    <text class="invite-text event-time" x="415" y="572" font-size="29">6-9 pm</text>

    <g class="divider">
      <line class="frame-line" x1="254" y1="608" x2="398" y2="608"/>
      <circle class="frame-line" cx="415" cy="608" r="6"/>
      <line class="frame-line" x1="432" y1="608" x2="576" y2="608"/>
    </g>

    <text class="invite-text rsvp" x="415" y="660" font-size="29">To RSVP send email to:</text>
    <text class="invite-text rsvp-email" x="415" y="700" font-size="26">@marisol@brix9legal.example</text>
    <text class="invite-text note" x="415" y="760" font-size="20">Note: The Quarry had a clear bag policy</text>
  </svg>

  <!-- Back: bag policy -->
  <svg class="card card--back" viewBox="0 0 820 1054" preserveAspectRatio="none" aria-label="Happy hour invitation, back: clear bag policy">
    <rect width="820" height="1054" fill="var(--card-dark)"/>
    <g class="frame-lines">
      <polyline class="frame-line" points="0,30 144,187"/>
      <polyline class="frame-line" points="553,0 553,140"/>
      <polyline class="frame-line" points="682,196 818,56"/>
      <polyline class="frame-line" points="144,693 194,750 0,953"/>
      <polyline class="frame-line" points="682,691 621,750 818,965"/>
      <polyline class="frame-line" points="682,691 769,785"/>
      <polyline class="frame-line" points="0,785 820,785"/>
      <polyline class="frame-line" points="221,785 404,985 404,1054"/>
      <polyline class="frame-line" points="553,843 553,1054"/>
    </g>

    <g class="policy-poster">
      <rect class="poster-body-panel" x="147" y="205" width="536" height="500" fill="var(--card-light)" stroke="var(--accent-blue)" stroke-width="1.6"/>
      <polygon class="poster-header" points="147,187 193,141 631,141 683,196 683,215 147,215" fill="var(--poster-navy)" stroke="var(--accent-blue)" stroke-width="1.6"/>
      <polygon class="poster-footer" points="147,690 683,690 623,750 650,785 167,785 195,750" fill="var(--poster-navy)" stroke="var(--accent-blue)" stroke-width="1.6"/>

      <circle cx="411" cy="158" r="4" fill="var(--poster-white)"/>
      <text class="poster-text poster-light center" x="411" y="187" font-size="23" font-weight="600" letter-spacing="7">THE QUARRY</text>
      <text class="poster-text poster-light center" x="411" y="206" font-size="14" letter-spacing="0.5">SPECIAL EVENT PROTOCOL</text>

      <rect x="205" y="230" width="413" height="47" fill="var(--poster-white)"/>
      <text class="poster-text poster-heading center" x="411" y="248" font-size="14">NO PURSES. CLEAR BAGS ONLY.</text>
      <text class="poster-text poster-body center" x="411" y="259" font-size="8">In an effort to enhance public safety, Vantage Hall has modified its security policy</text>
      <text class="poster-text poster-body center" x="411" y="270" font-size="8">by limiting the size and style of bags allowed in the venue.</text>

      <!-- Approved -->
      <text class="poster-text poster-heading" x="206" y="311" font-size="13">APPROVED BAGS</text>
      <circle cx="337" cy="306" r="6" fill="var(--approve-green)"/>
      <polyline points="334,306 336.5,308.5 340.5,303.5" fill="none" stroke="var(--poster-white)" stroke-width="1.5"/>

      <text class="poster-text poster-body" x="206" y="336" font-size="8.5" font-weight="700">CLEAR TOTE</text>
      <text class="poster-text poster-body" x="206" y="347" font-size="7.5">Plastic, vinyl or PVC</text>
      <text class="poster-text poster-body" x="206" y="358" font-size="7.5">and do not exceed</text>
      <text class="poster-text poster-body" x="206" y="369" font-size="7.5">12"x6"x12"</text>

      <text class="poster-text poster-body" x="317" y="336" font-size="8.5" font-weight="700">PLASTIC</text>
      <text class="poster-text poster-body" x="317" y="347" font-size="8.5" font-weight="700">STORAGE BAG</text>
      <text class="poster-text poster-body" x="317" y="358" font-size="7.5">Clear, one (1) gallon,</text>
      <text class="poster-text poster-body" x="317" y="369" font-size="7.5">re-sealable</text>

      <rect x="206" y="379" width="87" height="80" fill="var(--poster-blue)" role="img" aria-label="Illustration of a clear tote bag with dimensions"/>
      <rect x="316" y="379" width="69" height="80" fill="var(--poster-blue)" role="img" aria-label="Illustration of a clear plastic storage bag"/>

      <g class="poster-text poster-body" font-size="8">
        <text x="206" y="484">•</text><text x="218" y="484">Approximately the size of a hand with</text>
        <text x="218" y="496">or without a handle or strap</text>
        <text x="206" y="511">•</text><text x="218" y="511">No larger than 4.5" x 6.5" with or</text>
        <text x="218" y="523">without a handle or strap</text>
        <text x="206" y="538">•</text><text x="218" y="538">Can be carried separately or within an</text>
        <text x="218" y="550">approved plastic bag</text>
      </g>

      <rect x="205" y="573" width="90" height="55" fill="var(--poster-blue)" role="img" aria-label="Illustration of a small clutch measuring 4.5 by 6.5 inches"/>
      <rect x="302" y="573" width="90" height="55" fill="var(--poster-blue)" role="img" aria-label="Illustration of a small wallet measuring 3.5 by 4 inches"/>
      <rect x="253" y="635" width="91" height="55" fill="var(--poster-blue)" role="img" aria-label="Illustration of a small pouch measuring 4.5 by 6.5 inches"/>

      <line x1="413" y1="300" x2="413" y2="690" stroke="var(--poster-navy)" stroke-width="1"/>

      <!-- Prohibited -->
      <text class="poster-text poster-heading" x="434" y="311" font-size="13">PROHIBITED BAGS</text>
      <circle cx="573" cy="306" r="6" fill="var(--prohibit-red)"/>
      <path d="M570.5,303.5 L575.5,308.5 M575.5,303.5 L570.5,308.5" stroke="var(--poster-white)" stroke-width="1.5"/>

      <g class="poster-text poster-body" font-size="8">
        <text x="434" y="333">•</text><text x="448" y="333">All purses, bags or containers larger</text>
        <text x="448" y="345">than a small clutch bag</text>
        <text x="434" y="358">•</text><text x="448" y="358">Backpacks</text>
        <text x="434" y="372">•</text><text x="448" y="372">Binocular case</text>
        <text x="448" y="382" font-size="6">Binoculars may be worn around the neck</text>
        <text x="434" y="395">•</text><text x="448" y="395">Briefcases</text>
        <text x="434" y="409">•</text><text x="448" y="409">Camera bags</text>
        <text x="434" y="423">•</text><text x="448" y="423">Cinch bags</text>
        <text x="434" y="437">•</text><text x="448" y="437">Computer bags</text>
        <text x="434" y="451">•</text><text x="448" y="451">Coolers</text>
        <text x="434" y="465">•</text><text x="448" y="465">Diaper bags</text>
        <text x="434" y="479">•</text><text x="448" y="479">Fanny packs</text>
        <text x="434" y="493">•</text><text x="448" y="493">Luggage of any kind</text>
        <text x="434" y="506">•</text><text x="448" y="506">Seat Cushion</text>
      </g>

      <rect x="434" y="520" width="185" height="143" fill="var(--poster-blue)" role="img" aria-label="Illustrations of prohibited bags: backpack, purse, camera case, binocular case, fanny pack, seat cushion, diaper bag and printed plastic bag"/>

      <text class="poster-text poster-body" x="434" y="682" font-size="5.5">*An exception will be made for medically necessary items</text>
      <text class="poster-text poster-body" x="434" y="690" font-size="5.5">after proper inspection at a gate designated for this purpose</text>

      <text class="poster-text poster-light center" x="411" y="723" font-size="11" font-weight="700">CLEAR BAGS AVAILABLE FOR PURCHASE</text>
      <text class="poster-text poster-light center" x="411" y="737" font-size="10">please ask your planner for more information and pricing</text>
    </g>
  </svg>

</main>
</body>
</html>
```